Saucy Velvet Impz Business Card

We need business cards designed for our consultants to use and hand out to customers.
We are an Adult party plan company (like Crelvaware but sex toys and lingerie)
We would like bright colours pinks, purples.
The cards need our logo
Space for the reps phone number email address and name.
We need our website on it www.saucyvelvetimps.com.au

```html
<!DOCTYPE html>
<html lang="en">
<head>
<meta charset="utf-8">
<title>Saucy Velvet Impz – Business Card</title>
<link rel="stylesheet" href="https://fonts.googleapis.com/css2?family=Amaranth:wght@400;700&display=swap">
<style>
  :root {
    --backdrop: #6c6f70;
    --card-top: #6e1148;
    --card-bottom: #b43f7e;
    --pattern-top: #7d1a55;
    --pattern-bottom: #a8376f;
    --brand-pink: #e25a9c;
    --ink: #0c0c0c;
  }
  * { box-sizing: border-box; margin: 0; padding: 0; }
  html, body { width: 1200px; height: 900px; overflow: hidden; }
  body {
    background: var(--backdrop);
    font-family: "Amaranth", sans-serif;
    position: relative;
  }
  .card {
    position: absolute;
    top: 180px;
    width: 330px;
    height: 540px;
    overflow: hidden;
    background: linear-gradient(180deg, var(--card-top) 0%, var(--card-bottom) 100%);
  }
  .card--front { left: 220px; }
  .card--back { left: 650px; }
  .card-pattern {
    position: absolute;
    inset: 0;
    background: linear-gradient(180deg, var(--pattern-top) 0%, var(--pattern-bottom) 100%);
    opacity: 0.55;
  }
  .brand {
    position: absolute;
    left: 0; right: 0;
    display: flex;
    align-items: center;
    justify-content: center;
    gap: 8px;
    color: var(--brand-pink);
    font-weight: 700;
    font-size: 27px;
    white-space: nowrap;
  }
  .brand-dot {
    width: 14px; height: 14px;
    border-radius: 50%;
    background: var(--brand-pink);
  }
  .card--front .brand { top: 245px; }
  .card--back .brand { top: 60px; }
  .rep {
    position: absolute;
    left: 40px;
    top: 150px;
    color: var(--ink);
  }
  .rep-name { font-size: 32px; font-weight: 700; line-height: 1.05; }
  .rep-phone {
    font-size: 22px; font-weight: 700;
    display: flex; align-items: center; gap: 4px;
  }
  .contacts {
    position: absolute;
    left: 40px;
    top: 258px;
    list-style: none;
    color: var(--ink);
    font-size: 15px;
  }
  .contacts li { display: flex; align-items: center; gap: 6px; margin-bottom: 6px; }
  .icon { width: 15px; height: 15px; flex: none; }
  .footer-band { position: absolute; left: 0; bottom: 0; width: 330px; height: 140px; }
</style>
</head>
<body>
  <section class="card card--front">
    <div class="card-pattern" role="img" aria-label="Faint damask floral pattern"></div>
    <div class="brand"><span class="brand-dot"></span>Saucy Velvet Impz</div>
  </section>

  <section class="card card--back">
    <div class="card-pattern" role="img" aria-label="Faint damask floral pattern"></div>
    <div class="brand"><span class="brand-dot"></span>Saucy Velvet Impz</div>

    <div class="rep">
      <p class="rep-name">Your Name</p>
      <p class="rep-phone">
        <svg class="icon" viewBox="0 0 16 16" aria-hidden="true"><path d="M4 2l2.5 3-1.5 1.5c1 2 2.5 3.5 4.5 4.5L11 9.5l3 2.5-1.5 2c-5 0-10.5-5.5-10.5-10.5z" fill="#0c0c0c"/></svg>
        0400•555•218
      </p>
    </div>

    <ul class="contacts">
      <li>
        <svg class="icon" viewBox="0 0 16 16" aria-hidden="true"><rect x="1" y="3" width="14" height="10" fill="none" stroke="#0c0c0c" stroke-width="1.5"/><path d="M1 3l7 6 7-6" fill="none" stroke="#0c0c0c" stroke-width="1.5"/></svg>
        saucyvelvetimps@domain.com
      </li>
      <li>
        <svg class="icon" viewBox="0 0 16 16" aria-hidden="true"><rect x="3" y="3" width="10" height="8" fill="none" stroke="#0c0c0c" stroke-width="1.5"/><path d="M1 13h14" stroke="#0c0c0c" stroke-width="2"/></svg>
        www.saucyvelvetimps.com.au
      </li>
    </ul>

    <svg class="footer-band" viewBox="0 0 330 140" aria-hidden="true">
      <polygon points="0,140 0,90 70,55 145,55 200,22 330,10 330,140" fill="#0c0c0c"/>
    </svg>
  </section>
</body>
</html>
```